Crestmoor Valor Cleaning Solutions

Need a logo and business card design. I want to use a translucent business card. I want to abbreviate the name C.V.C.S. Commercial Cleaning, because my is Tam. I’d also like to incorporate a knight or something like that. I want the idea to tie in with the word Crestmoor. New ideas are welcome, i don’t want to limit anyone’s creativity.

Target Market(s)

Commercial Cleaning for businesses.

Contact Information for Business Card

Crestmoor
Valor
Cleaning
Solutions

```html
<!DOCTYPE html>
<html lang="en">
<head>
<meta charset="utf-8">
<title>Crestmoor Valor Cleaning Solutions – Business Card</title>
<link rel="stylesheet" href="https://fonts.googleapis.com/css2?family=Roboto:wght@300;400;500;700&display=swap">
<style>
  :root {
    --page-bg: #e9edf2;
    --card-bg: #fbfcfd;
    --navy: #1d2f72;
    --navy-deep: #18296a;
    --sky: #2e9ad6;
    --orange: #f07f1a;
    --ink: #1f1f24;
    --contact-text: #e6eaf4;
    --icon-blue: #3ea2e0;
    --mark-tint: #bfe0f5;
  }
  html, body {
    margin: 0;
    width: 1200px;
    height: 900px;
    overflow: hidden;
    background: var(--page-bg);
    font-family: "Roboto", Arial, sans-serif;
  }
  .business-card {
    position: absolute;
    left: 100px;
    top: 163px;
    width: 1000px;
    height: 572px;
    border-radius: 22px;
    background: var(--card-bg);
    overflow: hidden;
    box-shadow: 0 10px 30px rgba(20, 40, 90, 0.18);
  }
  .card-waves {
    position: absolute;
    inset: 0;
    width: 100%;
    height: 100%;
  }
  .brand-mark {
    position: absolute;
    left: 82px;
    top: 48px;
    width: 150px;
    height: 150px;
    background: var(--mark-tint);
  }
  .brand-name {
    position: absolute;
    left: 276px;
    top: 62px;
    margin: 0;
    color: var(--navy);
    font-weight: 700;
    line-height: 1.02;
  }
  .brand-name .line-main { display: block; font-size: 56px; letter-spacing: -0.5px; }
  .brand-name .line-sub { display: block; font-size: 40px; margin-top: 4px; }
  .tagline {
    position: absolute;
    left: 278px;
    top: 192px;
    margin: 0;
    color: var(--orange);
    font-size: 21px;
    font-weight: 400;
  }
  .holder {
    position: absolute;
    left: 78px;
    top: 322px;
  }
  .holder-name {
    margin: 0;
    font-size: 31px;
    font-weight: 400;
    color: var(--ink);
  }
  .holder-title {
    margin: 4px 0 0;
    font-size: 21px;
    font-weight: 400;
    color: var(--navy);
  }
  .contact-list {
    position: absolute;
    right: 64px;
    top: 384px;
    margin: 0;
    padding: 0;
    list-style: none;
  }
  .contact-item {
    display: flex;
    justify-content: flex-end;
    align-items: center;
    gap: 14px;
    height: 34px;
    color: var(--contact-text);
    font-size: 20px;
    font-weight: 400;
    letter-spacing: 0.3px;
  }
  .contact-icon {
    width: 20px;
    height: 20px;
    fill: var(--icon-blue);
  }
</style>
</head>
<body>
  <main class="business-card">
    <svg class="card-waves" viewBox="0 0 1000 572" preserveAspectRatio="none" aria-hidden="true">
      <path fill="var(--navy)" d="M0,478 C260,468 520,360 720,306 C830,276 920,266 1000,264 L1000,572 L0,572 Z"/>
      <path fill="var(--navy-deep)" d="M0,438 C230,440 470,330 660,270 C780,232 870,222 920,226 C840,226 760,246 660,284 C470,356 250,458 0,462 Z"/>
      <path fill="var(--sky)" d="M0,420 C170,418 330,398 490,362 C360,410 180,446 0,456 Z"/>
    </svg>

    <div class="brand-mark" aria-hidden="true"></div>
    <h1 class="brand-name">
      <span class="line-main">Crestmoor Valor</span>
      <span class="line-sub">Cleaning Solutions</span>
    </h1>
    <p class="tagline">C.V.C.S. Commercial Cleaning</p>

    <section class="holder">
      <p class="holder-name">Marcus Ellery</p>
      <p class="holder-title">CEO/Founder</p>
    </section>

    <ul class="contact-list">
      <li class="contact-item">555-013-2840
        <svg class="contact-icon" viewBox="0 0 24 24" aria-label="Phone"><path d="M6.6 10.8c1.4 2.8 3.8 5.1 6.6 6.6l2.2-2.2c.3-.3.7-.4 1-.2 1.1.4 2.3.6 3.6.6.6 0 1 .4 1 1V20c0 .6-.4 1-1 1C10.6 21 3 13.4 3 4c0-.6.4-1 1-1h3.5c.6 0 1 .4 1 1 0 1.3.2 2.5.6 3.6.1.3 0 .7-.2 1z"/></svg>
      </li>
      <li class="contact-item">555-013-2840
        <svg class="contact-icon" viewBox="0 0 24 24" aria-label="Fax"><path d="M7 3h10v4H7zM4 8h16a2 2 0 0 1 2 2v6h-4v5H6v-5H2v-6a2 2 0 0 1 2-2zm4 7v4h8v-4z"/></svg>
      </li>
      <li class="contact-item">owen@cvcsmail.com
        <svg class="contact-icon" viewBox="0 0 24 24" aria-label="Email"><path d="M2 5h20v14H2zm2 2v.4l8 5.3 8-5.3V7zm0 2.8V17h16V9.8l-8 5.3z"/></svg>
      </li>
      <li class="contact-item">www.cvcsclean.com
        <svg class="contact-icon" viewBox="0 0 24 24" aria-label="Website"><path d="M12 2a10 10 0 1 0 0 20 10 10 0 0 0 0-20zm6.9 6h-2.8a15 15 0 0 0-1.3-3.6A8 8 0 0 1 18.9 8zM12 4c.8 1.1 1.5 2.5 1.9 4h-3.8c.4-1.5 1.1-2.9 1.9-4zM4.3 14a8 8 0 0 1 0-4h3.2a16 16 0 0 0 0 4zm.8 2h2.8c.3 1.3.8 2.5 1.3 3.6A8 8 0 0 1 5.1 16zm2.8-8H5.1a8 8 0 0 1 4.1-3.6C8.7 5.5 8.2 6.7 7.9 8zM12 20c-.8-1.1-1.5-2.5-1.9-4h3.8c-.4 1.5-1.1 2.9-1.9 4zm2.3-6H9.7a14 14 0 0 1 0-4h4.6a14 14 0 0 1 0 4zm.5 5.6c.5-1.1 1-2.3 1.3-3.6h2.8a8 8 0 0 1-4.1 3.6zm1.7-5.6a16 16 0 0 0 0-4h3.2a8 8 0 0 1 0 4z"/></svg>
      </li>
    </ul>
  </main>
</body>
</html>
```